New Meal Prep Flyer for New Package Deals

We are looking for a design that displays our new packages that we offer. If you take a look at our website www.copperspoonpantry.com, and click on packages , you'll see the way we display them currently . We would like something similar to that in style . The first package is called "Evergreen" and this package will be a 1 week package (7 days ), 2 meals a day, for a price of $195.00. The second package is called "Pebble" and this package will be a 3 week package (21 days) 2 meals per day, for a price of $546.00 , the third package is a 6 week+ package (45 days), and it is called "Lighthouse" , 2 meals per day , and the price is $1080.00 .
For the Pebble Package , can you put next to it "Save $42.00!"
For the Lighthouse Package, can you put next to it "Save $180!"
We also want our logo on the flyer (see attached), and we are just looking for a 1 page flyer , 8 1/2 x 11.

```html
<!DOCTYPE html>
<html lang="en">
<head>
<meta charset="utf-8">
<title>Copper Spoon – Our New Packages</title>
<link href="https://fonts.googleapis.com/css2?family=Bebas+Neue&family=Montserrat:wght@600;700;800&display=swap" rel="stylesheet">
<style>
:root{
  --green:#8dbf24;
  --green-dark:#7aa81c;
  --charcoal:#2b2b2b;
  --band:#474747;
  --footer:#4d4d4d;
  --card:#f2f2f2;
  --ink:#2e2e2e;
  --page:#6a6a6a;
  --white:#ffffff;
}
*{margin:0;padding:0;box-sizing:border-box}
html,body{width:990px;height:1200px;overflow:hidden;background:var(--page)}
.flyer{position:absolute;left:31px;top:0;width:928px;height:1200px;background:var(--white);overflow:hidden;font-family:'Montserrat',sans-serif}
.hero{position:absolute;left:0;top:0;width:928px;height:472px;
  background:radial-gradient(ellipse at 45% 45%,#6b5a3e 0%,#3f3426 45%,#242220 100%)}
.hero::after{content:"";position:absolute;inset:0;background:rgba(20,20,20,.35)}
.brand{position:absolute;left:0;top:140px;width:928px;text-align:center;z-index:2;
  font-weight:800;font-size:68px;letter-spacing:1px;color:#c9c9c9;line-height:1}
.tagline{position:absolute;left:0;top:228px;width:928px;text-align:center;z-index:2;
  font-weight:800;font-size:33px;color:var(--green);letter-spacing:-.5px}
.tagline .divider{display:inline-block;width:3px;height:36px;background:var(--green);vertical-align:-6px;margin:0 22px}
.gallery{position:absolute;top:371px;left:78px;display:flex;gap:15px}
.gallery .photo{width:247px;height:203px;position:relative}
.gallery .photo::after{content:"";position:absolute;left:9px;top:9px;right:9px;bottom:9px;border:1px solid var(--green)}
.photo.shrimp{background:linear-gradient(135deg,#c9a67a,#d98a3d 55%,#7a6a4a)}
.photo.bowls{background:linear-gradient(135deg,#6e8c3b,#c2a56a 50%,#d1b08a)}
.photo.waffle{background:linear-gradient(135deg,#dfe4e8,#d6a35e 50%,#c2c8cf)}
.section-title{position:absolute;top:608px;left:0;width:928px;text-align:center;
  font-family:'Bebas Neue',sans-serif;font-size:76px;color:var(--charcoal);line-height:1}
.rule{position:absolute;top:638px;width:111px;height:3px;background:var(--green)}
.rule.left{left:78px}.rule.right{left:739px}
.packages{position:absolute;top:702px;left:78px;display:flex;gap:16px}
.package{width:247px;height:285px;border-radius:6px;overflow:hidden;
  background:linear-gradient(90deg,#e6e6e6,#fafafa 50%,#e6e6e6);border:1px solid #d6d6d6;position:relative;text-align:center;color:var(--ink)}
.package .name{height:63px;background:var(--green);border-bottom:2px solid #3a3a3a;
  font-family:'Bebas Neue',sans-serif;font-size:38px;color:var(--white);line-height:66px}
.package .term{margin-top:10px;font-weight:700;font-size:17px;line-height:23px}
.package .sep{width:182px;height:1px;background:#555;margin:9px auto 8px}
.package .meals{font-weight:700;font-size:17px;line-height:20px}
.package .price{position:absolute;top:173px;left:0;right:0;height:49px;background:var(--band);
  color:var(--white);font-weight:800;font-size:35px;line-height:49px}
.package .save{position:absolute;top:222px;left:0;right:0;height:63px;background:var(--green);
  font-family:'Bebas Neue',sans-serif;font-size:36px;color:var(--white);line-height:66px}
.footer{position:absolute;left:0;top:1070px;width:928px;height:130px;background:var(--footer)}
.app-bar{position:absolute;top:1034px;left:75px;width:778px;height:67px;background:var(--white);
  border:1.5px solid var(--green);border-radius:3px;display:flex;align-items:center;padding-left:32px}
.store-badge{width:127px;height:37px;background:#111;border-radius:5px;margin-right:11px}
.app-bar .cta{margin-left:12px;font-weight:800;font-size:21px;color:#1d1d1d;letter-spacing:.6px}
.contact{position:absolute;top:1115px;left:0;width:928px;display:flex;justify-content:center;align-items:center;
  color:var(--white);font-weight:600;font-size:21px;white-space:nowrap}
.contact .accent{color:var(--green)}
.contact .bar{color:var(--green);margin:0 14px}
.contact .follow{color:var(--green);font-weight:800;font-size:17px;letter-spacing:.5px;margin-right:12px}
.contact .dot{width:20px;height:20px;border-radius:50%;background:var(--green);margin-right:12px}
.contact svg{margin-right:10px}
</style>
</head>
<body>
<main class="flyer">
  <header class="hero" role="img" aria-label="Photo of a roasted vegetable and poached egg bowl with greens"></header>
  <div class="brand">COPPER SPOON</div>
  <div class="tagline">HEALTHY KITCHEN<span class="divider"></span>MEAL PREP</div>

  <section class="gallery">
    <div class="photo shrimp" role="img" aria-label="Photo of shrimp and vegetable curry bowl"></div>
    <div class="photo bowls" role="img" aria-label="Photo of grain, beet and vegetable meal prep bowls"></div>
    <div class="photo waffle" role="img" aria-label="Photo of a waffle topped with berries and yogurt"></div>
  </section>

  <span class="rule left"></span>
  <h1 class="section-title">OUR NEW PACKAGES</h1>
  <span class="rule right"></span>

  <section class="packages">
    <article class="package">
      <h2 class="name">EVERGREEN</h2>
      <p class="term">1 week<br>package (7 days)</p>
      <div class="sep"></div>
      <p class="meals">2 meals a day</p>
      <p class="price">$195.00</p>
    </article>
    <article class="package">
      <h2 class="name">PEBBLE</h2>
      <p class="term">3 week<br>package (21 days)</p>
      <div class="sep"></div>
      <p class="meals">2 meals a day</p>
      <p class="price">$546.00</p>
      <p class="save">SAVE $42.00!</p>
    </article>
    <article class="package">
      <h2 class="name">LIGHTHOUSE</h2>
      <p class="term">6 week+<br>package (45 days)</p>
      <div class="sep"></div>
      <p class="meals">2 meals a day</p>
      <p class="price">$1080.00</p>
      <p class="save">SAVE $180!</p>
    </article>
  </section>

  <footer class="footer"></footer>
  <div class="app-bar">
    <span class="store-badge"></span>
    <span class="store-badge"></span>
    <span class="cta">ORDER FOOD EASILY ON OUR APP</span>
  </div>
  <div class="contact">
    <svg width="18" height="18" viewBox="0 0 20 20" fill="none" stroke="#8dbf24" stroke-width="1.5">
      <circle cx="10" cy="10" r="8.5"/><ellipse cx="10" cy="10" rx="3.8" ry="8.5"/><path d="M1.5 10h17M3 5.5h14M3 14.5h14"/>
    </svg>
    <span>www.<span class="accent">copperspoonpantry</span>.com</span>
    <span class="bar">|</span>
    <span class="follow">FOLLOW US</span>
    <span class="dot"></span>
    <span>/copperspoonpantry/</span>
  </div>
</main>
</body>
</html>
```